Label Design Project for my tea product Imported from Japan

I have a tea importing business. I want someone to help me design a label for my Uji matcha tea product. I want the label to be modern, neat, and beautifully designed. I prefer it to be easily adaptable to other tea products that I will be importing.
Product name: Organic Uji Matcha
Company name: Calm Harbor Leaf Merchants
Description: Powdered Green Tea Matcha
Ceremonial grade premium quality
Directly imported from Japan
This product is going to be sold in the U.S. market, so please make sure that the label is in compliance with the FDA regulations.

Target Market(s)

High end tea consumers

Industry/Entity Type

Business

Requirements
Must have
• Marking of origin : product of Japan
• Imported by: Calm Harbor Leaf Merchants
• Leave space for Net weight, the name and place of business of the manufacturer.
• Ingredients: Green Tea 100%
• Nutrition list is not necessary.

```html
<!DOCTYPE html>
<html lang="en">
<head>
<meta charset="utf-8">
<title>Organic Uji Matcha Label</title>
<link rel="stylesheet" href="https://fonts.googleapis.com/css2?family=Philosopher:ital,wght@1,700&family=Tinos:wght@400&family=Courgette&display=swap">
<style>
  :root {
    --green-deep: #1d6b2f;
    --green-band: #23873a;
    --green-mid: #5cab2f;
    --green-lime: #a6d14a;
    --green-pale: #f1f7de;
    --olive: #7d8a3c;
    --olive-dark: #5f6b2a;
    --cream: #fbf6df;
    --white: #ffffff;
    --red-stamp: #d3202a;
    --photo-light: #8fb84a;
    --photo-dark: #5e8f28;
  }
  html, body {
    margin: 0;
    padding: 0;
    overflow: hidden;
    background: #ffffff;
  }
  .label {
    position: relative;
    width: 720px;
    height: 1200px;
    overflow: hidden;
    background: radial-gradient(ellipse at 35% 45%, var(--green-pale) 0%, #dfeeb4 45%, var(--green-lime) 80%, var(--green-mid) 100%);
    font-family: "Tinos", serif;
  }
  .label__art {
    position: absolute;
    inset: 0;
  }
  .brand {
    position: absolute;
    left: 60px;
    top: 172px;
    width: 538px;
    color: var(--green-deep);
    font-family: "Tinos", serif;
    font-weight: 400;
    text-transform: uppercase;
  }
  .brand__line1 {
    display: block;
    font-size: 42px;
    letter-spacing: 4px;
    text-align: right;
    line-height: 1;
  }
  .brand__line2 {
    display: block;
    font-size: 20px;
    letter-spacing: 2px;
    text-align: right;
    margin-top: 14px;
  }
  .product {
    position: absolute;
    left: 0;
    width: 720px;
    text-align: center;
    color: var(--green-deep);
    font-family: "Philosopher", sans-serif;
    font-style: italic;
    font-weight: 700;
    margin: 0;
  }
  .product--organic { top: 262px; font-size: 100px; line-height: 1; }
  .product--name { top: 404px; font-size: 108px; line-height: 1; }
  .descriptor {
    position: absolute;
    top: 556px;
    left: 0;
    width: 720px;
    text-align: center;
    color: var(--green-deep);
    font-size: 40px;
    line-height: 1;
    margin: 0;
  }
  .quality {
    position: absolute;
    top: 650px;
    left: 0;
    width: 720px;
    text-align: center;
    color: var(--cream);
    font-family: "Courgette", cursive;
    font-size: 36px;
    line-height: 1;
    margin: 0;
  }
  .origin {
    position: absolute;
    left: 551px;
    top: 942px;
    width: 132px;
    height: 132px;
    border-radius: 50%;
    background: var(--white);
    box-shadow: inset 0 0 0 9px var(--red-stamp);
    display: flex;
    flex-direction: column;
    align-items: center;
    justify-content: center;
    font-family: "Tinos", serif;
    line-height: 1;
  }
  .origin__small { font-size: 17px; color: var(--red-stamp); }
  .origin__big { font-size: 30px; color: var(--red-stamp); font-weight: 400; }
  .facts {
    position: absolute;
    left: 44px;
    top: 1084px;
    color: var(--white);
  }
  .facts__ingredients { font-size: 25px; line-height: 1; margin: 0 0 14px; }
  .facts__line { font-size: 19px; line-height: 1; margin: 0 0 6px; }
  .net-weight {
    position: absolute;
    left: 552px;
    top: 1124px;
    color: var(--white);
    font-size: 25px;
    line-height: 1;
    margin: 0;
  }
</style>
</head>
<body>
<main class="label">
  <svg class="label__art" width="720" height="1200" viewBox="0 0 720 1200" xmlns="http://www.w3.org/2000/svg">
    <defs>
      <linearGradient id="photoFill" x1="0" y1="0" x2="0" y2="1">
        <stop offset="0" stop-color="var(--photo-light)" stop-opacity="0.55"/>
        <stop offset="1" stop-color="var(--photo-dark)" stop-opacity="0.9"/>
      </linearGradient>
    </defs>
    <path d="M0 0 H720 V40 C600 50 470 60 380 120 C300 170 220 200 120 230 C70 245 30 255 0 260 Z" fill="var(--green-band)"/>
    <path d="M0 260 C30 255 70 245 120 230 C220 200 300 170 380 120 C470 60 600 50 720 40 V58 C610 66 490 80 400 135 C310 190 210 225 110 250 C60 262 25 268 0 270 Z" fill="var(--green-lime)"/>
    <g class="ribbon">
      <polygon points="128,640 178,640 178,712 153,712 166,676" fill="var(--olive-dark)"/>
      <polygon points="592,640 542,640 542,712 567,712 554,676" fill="var(--olive-dark)"/>
      <path d="M158 632 Q360 616 562 632 L562 704 Q360 688 158 704 Z" fill="var(--olive)"/>
    </g>
    <rect class="product-photo" role="img" aria-label="Photo of a mound of bright green matcha powder beside a fresh tea sprig" x="0" y="722" width="490" height="340" fill="url(#photoFill)"/>
    <path d="M0 1000 C200 950 450 930 720 850 V905 C470 975 230 1000 0 1030 Z" fill="var(--white)" opacity="0.85"/>
    <path d="M0 1056 C230 1030 470 1000 720 930 V1200 H0 Z" fill="var(--green-band)"/>
  </svg>

  <div class="brand">
    <span class="brand__line1">Calm Harbor</span>
    <span class="brand__line2">Leaf Merchants</span>
  </div>

  <h1 class="product product--organic">Organic</h1>
  <h1 class="product product--name">Uji Matcha</h1>
  <p class="descriptor">Powdered Green Tea Matcha</p>
  <p class="quality">Premium Quality</p>

  <div class="origin">
    <span class="origin__small">made in</span>
    <span class="origin__big">japan</span>
  </div>

  <div class="facts">
    <p class="facts__ingredients">Ingredients: Green Tea 100%</p>
    <p class="facts__line">Imported by :&nbsp; Calm Harbor Leaf Merchants</p>
    <p class="facts__line">Manufactured by : .</p>
  </div>
  <p class="net-weight">Nett.Wt.</p>
</main>
</body>
</html>
```